Realty Group Needs Classy, Contemporary Letterhead Design

We need a letterhead design for a new realty company located in NY, USA. We buy investment properties to rehabilitate and or keep in our rental portfolio.

```html
<!DOCTYPE html>
<html lang="en">
<head>
<meta charset="utf-8">
<title>Halvorsen Realty Group – Letterhead &amp; Folder</title>
<link href="https://fonts.googleapis.com/css2?family=Open+Sans:wght@400;600;700&display=swap" rel="stylesheet">
<style>
  :root{
    --bg:#3a3d3d;
    --paper:#ffffff;
    --folder:#f1f1f1;
    --ink:#2b2b2b;
    --muted:#5a5a5a;
    --purple:#4a2a8c;
    --purple-deep:#3b1d74;
    --purple-light:#7656b4;
    --ghost:#ececec;
  }
  *{margin:0;padding:0;box-sizing:border-box}
  html,body{width:1200px;height:900px;overflow:hidden;background:var(--bg);font-family:"Open Sans",sans-serif}
  .stage{position:relative;width:1200px;height:900px}

  .folder-spread{position:absolute;left:176px;top:286px;width:535px;height:379px;background:var(--folder);box-shadow:0 6px 18px rgba(0,0,0,.35)}
  .folder-spread__fold{position:absolute;left:267px;top:0;width:1px;height:100%;background:#dcdcdc}
  .pocket{position:absolute;left:345px;top:303px;width:190px;height:76px}
  .pocket__name{position:absolute;left:95px;top:34px;font-weight:700;font-size:10px;color:rgba(255,255,255,.12);letter-spacing:.3px}

  .letterhead{position:absolute;left:181px;top:292px;width:259px;height:366px;background:var(--paper);box-shadow:0 2px 6px rgba(0,0,0,.15)}
  .brand{position:absolute;text-align:center;color:var(--purple);font-weight:700;line-height:1}
  .letterhead .brand{left:0;width:100%;top:58px}
  .brand__name{font-size:10.5px;letter-spacing:.2px}
  .brand__sub{display:inline-block;margin-top:2px;font-size:3.4px;font-weight:700;padding:0 6px;border-top:0;position:relative}
  .brand__sub::before,.brand__sub::after{content:"";position:absolute;top:50%;width:10px;height:.5px;background:currentColor}
  .brand__sub::before{right:100%}
  .brand__sub::after{left:100%}

  .letter__title{position:absolute;left:32px;top:102px;font-size:5.2px;color:var(--ink)}
  .letter__body{position:absolute;left:32px;top:120px;width:199px;font-size:3.6px;line-height:6.7px;color:var(--muted);text-align:justify}
  .letter__body p+p{margin-top:0}
  .letter__body p.gap{margin-top:6.7px}
  .letter__sign-name{position:absolute;left:32px;top:245px;font-size:4.4px;color:var(--ink)}
  .letter__sign-role{position:absolute;left:32px;top:253px;font-size:2.2px;color:var(--muted)}
  .letter__signature{position:absolute;left:32px;top:262px;width:24px;height:14px;background:#f4f4f4;border-radius:2px}
  .letter__art{position:absolute;left:56px;top:232px;width:198px;height:130px;background:radial-gradient(ellipse at 55% 60%,var(--ghost),rgba(255,255,255,0) 70%)}
  .contacts{position:absolute;left:32px;top:317px;list-style:none;font-size:2.6px;color:var(--muted);line-height:5px}
  .contacts li{display:flex;align-items:center;gap:3px}
  .contacts svg{width:3.4px;height:3.4px}

  .cover{position:absolute;left:772px;top:287px;width:267px;height:376px;background:linear-gradient(160deg,var(--purple-deep) 0%,#4b2b90 45%,var(--purple-light) 100%);box-shadow:0 6px 18px rgba(0,0,0,.35)}
  .cover .brand{left:158px;top:175px;color:#fff}
  .cover__art{position:absolute;left:2px;top:198px;width:265px;height:178px;background:radial-gradient(ellipse at 60% 65%,rgba(255,255,255,.10),rgba(255,255,255,0) 70%)}
</style>
</head>
<body>
<main class="stage">

  <section class="folder-spread" aria-label="Presentation folder, inside">
    <div class="folder-spread__fold"></div>
    <svg class="pocket" viewBox="0 0 190 76" aria-hidden="true">
      <defs>
        <linearGradient id="pocketFill" x1="0" y1="0" x2="1" y2="1">
          <stop offset="0" stop-color="#6a48a8"/>
          <stop offset="1" stop-color="#5a3b9c"/>
        </linearGradient>
      </defs>
      <path d="M0 76 C8 20 30 0 70 0 L190 0 L190 76 Z" fill="url(#pocketFill)"/>
    </svg>
    <span class="pocket__name" style="left:455px;top:337px;position:absolute">HALVORSEN</span>
  </section>

  <article class="letterhead" aria-label="Letterhead">
    <div class="brand">
      <div class="brand__name">HALVORSEN</div>
      <span class="brand__sub">Realty Group, LLC</span>
    </div>

    <h1 class="letter__title" style="font-weight:400">Lorem ipsum</h1>

    <div class="letter__body">
      <p>Lorem ipsum dolor sit amet, consectetuer adipiscing elit, sed diam nonummy nibh euismod tincidunt ut laoreet dolore magna aliquam erat volutpat. Ut wisi enim ad minim veniam, quis nostrud exerci tation ullamcorper suscipit lobortis nisl ut aliquip ex ea commodo consequat. Duis autem vel eum iriure dolor in hendrerit in vulputate velit esse molestie consequat, vel illum dolore eu feugiat nulla facilisis at vero eros et accumsan et iusto odio dignissim qui blandit praesent luptatum zzril delenit augue duis dolore te feugait nulla facilisi.</p>
      <p>Lorem ipsum dolor sit amet, cons ectetuer adipiscing elit, sed diam nonummy nibh euismod tincidunt ut laoreet dolore magna aliquam erat volutpat. Ut wisi enim ad minim veniam, quis nostrud exerci tation ullamcorper suscipit lobortis nisl ut aliquip ex ea commodo consequat.</p>
      <p class="gap">Lorem ipsum dolor sit amet, consectetuer adipiscing elit, sed diam nonummy nibh euismod tincidunt ut laoreet dolore magna aliquam erat volutpat. Ut wisi enim ad minim veniam, quis nostrud exerci tation ullamcorper suscipit lobortis nisl ut aliquip ex ea commodo consequat. Duis autem vel eum iriure dolor in hendrerit in vulputate velit esse molestie consequat, vel illum dolore eu feugiat nulla facilisis at vero eros et accumsan et iusto odio dignissim qui blandit praesent luptatum zzril delenit augue duis dolore te feugait nulla facilisi.</p>
      <p>Lorem ipsum dolor sit amet, cons ectetuer adipiscing elit, sed diam nonummy nibh euismod tincidunt ut laoreet dolore magna aliquam erat volutpat. Ut wisi enim ad minim veniam, quis nostrud exerci tation ullamcorper suscipit lobortis nisl ut aliquip ex ea commodo consequat.</p>
    </div>

    <div class="letter__sign-name">Your name</div>
    <div class="letter__sign-role">Co-Founder &amp; CEO</div>
    <div class="letter__signature" role="img" aria-label="Handwritten signature"></div>

    <div class="letter__art" role="img" aria-label="Faint illustration of an archer drawing a bow"></div>

    <ul class="contacts">
      <li><svg viewBox="0 0 10 10"><rect width="10" height="10" rx="2" fill="#4a2a8c"/><path d="M3 2.5 L4.3 2.5 L4.8 4 L4 4.6 Q4.8 6 5.8 6.4 L6.4 5.6 L7.8 6.2 L7.8 7.4 Q4 7.6 2.6 3.2 Z" fill="#fff"/></svg>123.000.2850</li>
      <li><svg viewBox="0 0 10 10"><rect width="10" height="10" rx="2" fill="#4a2a8c"/><rect x="2.2" y="3" width="5.6" height="4" fill="none" stroke="#fff" stroke-width=".8"/><path d="M2.2 3 L5 5.2 L7.8 3" fill="none" stroke="#fff" stroke-width=".8"/></svg>youremail@gmail.com</li>
      <li><svg viewBox="0 0 10 10"><rect width="10" height="10" rx="2" fill="#4a2a8c"/><circle cx="5" cy="5" r="2.8" fill="none" stroke="#fff" stroke-width=".8"/><path d="M2.2 5 H7.8" stroke="#fff" stroke-width=".7"/></svg>yourwebsite.com</li>
      <li><svg viewBox="0 0 10 10"><rect width="10" height="10" rx="2" fill="#4a2a8c"/><path d="M5 8 Q2.6 5.4 2.6 4.2 A2.4 2.4 0 0 1 7.4 4.2 Q7.4 5.4 5 8 Z" fill="#fff"/><circle cx="5" cy="4.2" r=".9" fill="#4a2a8c"/></svg>your address 1234</li>
    </ul>
  </article>

  <section class="cover" aria-label="Presentation folder, front cover">
    <div class="brand">
      <div class="brand__name">HALVORSEN</div>
      <span class="brand__sub">Realty Group, LLC</span>
    </div>
    <div class="cover__art" role="img" aria-label="Faint tonal illustration of an archer drawing a bow"></div>
  </section>

</main>
</body>
</html>
```